Artificial intelligence, machine learning, and automation company needs a sexy business card design

We need a sleek and sexy business card design for an AI consulting company based in Philadelphia PA. We provide custom machine learning and automation solutions for companies of all shapes and sizes. The primary industries that we serve are pharmaceuticals, engineering, healthcare, and computer software. We would like the designs to be a black business card that uses green as a sleek accent color. The final design should communicate intelligence, cutting edge new-tech, and optimization.

Target Market(s)

C-level and VP level executives of multi-million annual companies. Mostly in Pharma, Healthcare, Real Estate, Retail, and Engineering

Industry/Entity Type

Computer Software

Contact Information for Business Card

Name: Jack Moss
Title: CEO
Cell: 215 604 8293
Email: JackM@quillarcworks.example
Website: www.QuillarcWorks.example

Font styles to use
Sans Serif

Colors

Designer to choose colors to be used in the design.

Requirements
Must have
• 1) Attached Quillarc Logo (either with colors or not/embossed)
• 2) "Artificial Intelligence" "Automation" and "Machine Learning"
• 3) "Quillarc Laboratories" or "Quillarc Works" or "Quillarc"
• 4) Sexy AF.
Nice to have
• Black card / dark card color, "Quillarc Green" accent colors (in attached .ai file), Embossment of logo/name/etc, thick card stock, colored borders (on card sides, not front/back faces)
Should not have
• Should not be bland, or unsexy.

```html
<!DOCTYPE html>
<html lang="en">
<head>
<meta charset="utf-8">
<title>Quillarc Laboratories – Business Card</title>
<link href="https://fonts.googleapis.com/css2?family=Montserrat:wght@400&family=Oswald:wght@600&family=Open+Sans:wght@400&display=swap" rel="stylesheet">
<style>
  :root {
    --page-bg: #e8e5e1;
    --card-bg: #242424;
    --accent: #5ccbaf;
    --text-light: #ffffff;
    --divider: #d9d9d9;
  }
  html, body {
    margin: 0;
    padding: 0;
    width: 1200px;
    height: 1000px;
    overflow: hidden;
    background: var(--page-bg);
  }
  .canvas {
    position: relative;
    width: 1200px;
    height: 1000px;
  }
  .card {
    position: absolute;
    left: 266px;
    width: 666px;
    height: 396px;
    background: var(--card-bg);
    box-shadow: 0 6px 18px rgba(0,0,0,0.25);
    overflow: hidden;
  }
  .card--front { top: 75px; }
  .card--back { top: 534px; }
  .card__band {
    position: absolute;
    left: 0;
    bottom: 0;
    width: 100%;
    height: 8px;
    background: var(--accent);
  }

  /* Front: brand lockup */
  .brand {
    position: absolute;
    left: 141px;
    top: 150px;
    display: flex;
    align-items: center;
    gap: 21px;
  }
  .brand__square {
    width: 88px;
    height: 88px;
    border: 4px solid var(--accent);
  }
  .brand__name {
    font-family: "Montserrat", sans-serif;
    font-weight: 400;
    color: var(--text-light);
    line-height: 1;
  }
  .brand__primary {
    display: block;
    font-size: 50px;
    letter-spacing: 3px;
  }
  .brand__secondary {
    display: block;
    margin-top: 12px;
    font-size: 24px;
    letter-spacing: 3.6px;
  }

  /* Back: contact block */
  .contact {
    position: absolute;
    top: 166px;
    left: 0;
    width: 100%;
    display: flex;
    justify-content: center;
    align-items: center;
  }
  .person {
    text-align: right;
    padding-right: 18px;
  }
  .person__name {
    font-family: "Oswald", sans-serif;
    font-weight: 600;
    font-size: 36px;
    line-height: 1;
    color: var(--accent);
    letter-spacing: 0.5px;
  }
  .person__title {
    margin-top: 6px;
    font-family: "Open Sans", sans-serif;
    font-size: 14px;
    color: var(--text-light);
  }
  .contact__divider {
    width: 1px;
    height: 56px;
    background: var(--divider);
  }
  .details {
    list-style: none;
    margin: 0;
    padding: 0 0 0 18px;
  }
  .details__item {
    display: flex;
    align-items: center;
    gap: 6px;
    font-family: "Open Sans", sans-serif;
    font-size: 15px;
    line-height: 20px;
    color: var(--text-light);
  }
  .details__icon {
    width: 14px;
    height: 14px;
    flex: none;
  }
</style>
</head>
<body>
<main class="canvas">
  <section class="card card--front" aria-label="Card front">
    <div class="brand">
      <div class="brand__square"></div>
      <div class="brand__name">
        <span class="brand__primary">QUILLARC</span>
        <span class="brand__secondary">LABORATORIES</span>
      </div>
    </div>
    <div class="card__band"></div>
  </section>

  <section class="card card--back" aria-label="Card back">
    <div class="contact">
      <div class="person">
        <div class="person__name">JACK MOSS</div>
        <div class="person__title">CEO</div>
      </div>
      <div class="contact__divider"></div>
      <ul class="details">
        <li class="details__item">
          <svg class="details__icon" viewBox="0 0 24 24" fill="none" stroke="#5ccbaf" stroke-width="2" stroke-linejoin="round"><path d="M5 3h4l2 5-2.5 1.5a11 11 0 0 0 6 6L16 13l5 2v4a2 2 0 0 1-2 2A17 17 0 0 1 3 5a2 2 0 0 1 2-2z"/></svg>
          215 604 8293
        </li>
        <li class="details__item">
          <svg class="details__icon" viewBox="0 0 24 24" fill="none" stroke="#5ccbaf" stroke-width="2"><rect x="3" y="5" width="18" height="14"/><path d="M3 5l9 8 9-8"/></svg>
          JackM@quillarcworks.example
        </li>
        <li class="details__item">
          <svg class="details__icon" viewBox="0 0 24 24" fill="none" stroke="#5ccbaf" stroke-width="2"><circle cx="12" cy="12" r="9"/><path d="M3 12h18M12 3c3 3 3 15 0 18M12 3c-3 3-3 15 0 18"/></svg>
          www.QuillarcWorks.example
        </li>
      </ul>
    </div>
    <div class="card__band"></div>
  </section>
</main>
</body>
</html>
```